Design for "Quiver" protein health bars wrappers

I need a new design for a protein bar that my partners and I are launching for the North American and European markets.
The bar's name is "Quiver."
Given the masculine/aggressive nature of that name, we are thinking of neutralizing it with a more feminine/soft font and design. But hey - the sky is the limit. We obviously want this 20-gram protein bar to sell to a wide net (not just men but women also). So if it means having a Zephyr Panel font/design (or whatever) in order to do this, so be it. I leave it up to your intelligence and experience.

The official name of the bar is just "QUIVER" (not "Quiver Protein").

We have six flavors divided into two categories, which are 1) SOFT and 2) CRUNCHY.
So, the idea is to make two similar designs for the wrapper that still distinguish themselves from each other because one is 'soft' and the other is 'crunchy.'
Then, within each category, the idea is to have three color variations, designating the three flavors in each category.

Please look at the dimensions and examples of the generic wrapper designs that we already have (and which we find too generic), which I have uploaded.

Target Market(s)

North America - Valmart, Green Basket
Europe - Norway, Sweden, Denmark, Germany, France, Switzerland, Italy.

Industry/Entity Type

Nutrition

Logo Text

Quiver

Font styles to use
Serif
Decorative

Colors
fff6dc
f04a50

Requirements
Must have
• The title is "Quiver".
• We have six flavors divided into two categories, which are 1) SOFT and 2) CRUNCHY.
• You can work on the two different types of similar-but-different designs for the "soft" and for the "cruncy." Then it's just a question of color variations for each flavor.
• The flavors are:
• SOFT: 1) strawberry, 2) Chocolate brownie, 3) Cinnamon Crunch
• CRUNCY: 1) Peanut, 2) Lemon, 3) Coconut.
• On the side or at the bottom, there should be stated:
• "20 gm protein"
• "children friendly"
Nice to have
• Obvious: a design that catches the eye and inspires someone to buy the bar to eat it.
• Part of the design could include a photograph of the actual bar (you can use generic photos for that until we place a pic of the actual bar). Like 1/4th of the total surface (or even a little smaller).

```html
<!DOCTYPE html>
<html lang="en">
<head>
<meta charset="utf-8">
<title>Quiver Soft Bars – Wrapper Range</title>
<link href="https://fonts.googleapis.com/css2?family=Oswald:wght@600;700&family=PT+Sans:wght@400;700&display=swap" rel="stylesheet">
<style>
  :root {
    --canvas: #ffffff;
    --cream: #f6efdf;
    --brand-red: #e0525a;
    --strawberry: #e8131a;
    --strawberry-photo: #c9262b;
    --cream-photo: #f4ece4;
    --brownie: #2e160b;
    --cinnamon: #b5621e;
    --cinnamon-text: #a8561a;
  }
  html, body {
    margin: 0;
    padding: 0;
    width: 1200px;
    height: 700px;
    overflow: hidden;
    background: var(--canvas);
  }
  .range { display: block; width: 1200px; height: 700px; }
  .wrapper-body { fill: var(--cream); }
  .wordmark {
    font-family: "Oswald", sans-serif;
    font-weight: 700;
    font-size: 66px;
    letter-spacing: 6px;
    fill: var(--brand-red);
  }
  .protein-claim, .net-weight {
    font-family: "PT Sans", sans-serif;
    font-weight: 400;
    font-size: 16px;
    fill: var(--brand-red);
  }
  .category {
    font-family: "PT Sans", sans-serif;
    font-weight: 700;
    font-size: 17px;
    fill: var(--brand-red);
  }
  .kids-claim {
    font-family: "PT Sans", sans-serif;
    font-weight: 700;
    font-size: 10px;
    fill: var(--brand-red);
  }
  .flavour {
    font-family: "Oswald", sans-serif;
    font-weight: 600;
    font-size: 19px;
    letter-spacing: 1.5px;
  }
  .flavour--strawberry { fill: var(--strawberry); }
  .flavour--brownie { fill: var(--brownie); }
  .flavour--cinnamon { fill: var(--cinnamon-text); }
</style>
</head>
<body>
<svg class="range" viewBox="0 0 1200 700" xmlns="http://www.w3.org/2000/svg">
  <defs>
    <linearGradient id="strawberry-shot" x1="0" y1="0" x2="1" y2="1">
      <stop offset="0" stop-color="#f1dcd6"/>
      <stop offset="0.45" stop-color="var(--cream-photo)"/>
      <stop offset="1" stop-color="var(--strawberry-photo)"/>
    </linearGradient>
    <linearGradient id="brownie-shot" x1="0" y1="0" x2="1" y2="1">
      <stop offset="0" stop-color="#3a1a0c"/>
      <stop offset="1" stop-color="#6a3620"/>
    </linearGradient>
    <linearGradient id="cinnamon-shot" x1="0" y1="0" x2="1" y2="1">
      <stop offset="0" stop-color="#a9603f"/>
      <stop offset="1" stop-color="#c98b6a"/>
    </linearGradient>
  </defs>

  <!-- Strawberry Cream Pie -->
  <g class="bar bar--strawberry">
    <path class="wrapper-end" fill="var(--strawberry)" d="M232 84 L322 72 L334 252 L250 256 L258 170 Z"/>
    <path class="wrapper-body" d="M320 72 L722 60 L722 246 L330 252 Z"/>
    <path role="img" aria-label="Photo of the strawberry cream pie bar" fill="url(#strawberry-shot)" d="M722 60 L780 30 L838 24 L850 130 L856 236 L722 246 Z"/>
    <line x1="722" y1="60" x2="722" y2="246" stroke="var(--strawberry)" stroke-width="6"/>
    <text class="protein-claim" x="592" y="89">20 gm protein</text>
    <text class="wordmark" x="334" y="182">QUIVER</text>
    <text class="category" x="437" y="213">SOFT</text>
    <text class="net-weight" x="400" y="243">Net Wt 2oz (54g)</text>
    <text class="flavour flavour--strawberry" text-anchor="end" x="712" y="141">STRAWBERRY</text>
    <text class="flavour flavour--strawberry" text-anchor="end" x="712" y="164">CREAM</text>
    <text class="flavour flavour--strawberry" text-anchor="end" x="712" y="187">PIE</text>
    <text class="kids-claim" x="604" y="224">children friendly</text>
  </g>

  <!-- Chocolate Brownie -->
  <g class="bar bar--brownie">
    <path class="wrapper-end" fill="var(--brownie)" d="M36 282 L118 274 L126 458 L42 466 L52 380 Z"/>
    <path class="wrapper-body" d="M118 274 L508 266 L508 452 L124 460 Z"/>
    <path role="img" aria-label="Photo of the chocolate brownie bar" fill="url(#brownie-shot)" d="M496 266 L640 262 L656 428 L512 448 Q490 360 496 266 Z"/>
    <text class="protein-claim" x="376" y="299">20 gm protein</text>
    <text class="wordmark" x="126" y="386">QUIVER</text>
    <text class="category" x="228" y="414">SOFT</text>
    <text class="net-weight" x="195" y="444">Net Wt 2oz (54g)</text>
    <text class="flavour flavour--brownie" x="386" y="342">CHOCOLATE</text>
    <text class="flavour flavour--brownie" x="386" y="364">BROWNIE</text>
    <text class="kids-claim" x="388" y="424">children friendly</text>
  </g>

  <!-- Cinnamon Crunch -->
  <g class="bar bar--cinnamon">
    <path class="wrapper-end" fill="var(--cinnamon)" d="M456 426 L540 414 L546 600 L462 608 L470 516 Z"/>
    <path class="wrapper-body" d="M540 414 L918 404 L918 582 L546 600 Z"/>
    <path role="img" aria-label="Photo of ground cinnamon crumble" fill="url(#cinnamon-shot)" d="M918 404 L1000 386 L1058 374 L1066 480 L1076 576 L918 582 Z"/>
    <line x1="918" y1="404" x2="918" y2="582" stroke="var(--cinnamon)" stroke-width="5"/>
    <text class="protein-claim" x="790" y="440">20 gm protein</text>
    <text class="wordmark" x="542" y="528">QUIVER</text>
    <text class="category" x="638" y="557">SOFT</text>
    <text class="net-weight" x="605" y="586">Net Wt 2oz (54g)</text>
    <text class="flavour flavour--cinnamon" x="808" y="486">CINNAMON</text>
    <text class="flavour flavour--cinnamon" x="808" y="508">CRUNCH</text>
    <text class="kids-claim" x="803" y="569">children friendly</text>
  </g>
</svg>
</body>
</html>
```